Spanish Student Needs a Cover for his PhD Dissertation

Hi everyone :) So, I'm a Corneal surgeon currently finishing my PhD, with a dissertation focused on the evaluation of quality of life in patients affected by a disease called Keratoconus. Just so you know, Keratoconus is a condition in which the cornea (the frontal part of the way) gets thin and bulgy and it decreases vision. What I did during my PhD was designing a questionnaire for evaluating quality of life in this kind of patients.
I need to design a hard cover for my dissertation, which is 200 sheets long. I like kind of minimalistic and geometric designs but I am totally open to suggestions. What needs to be in the cover is the name of the dissertation "Diseño, desarrollo y validación de una encuesta para evaluar el compromiso visual y emocional subjetivos en pacientes con Queratocono" and my name, "Iñigo Zabaleta". The other thing that needs to go there is the logo of my university (Universidad de Montealto). Aside from that, anything else is up to the designer. It would be important to use the kind of "red" color I am using in the dissertation. I am attaching the frontal page of my dissertation so you know what kind of design and colors I am using.
In the back part, of the cover, there should be this small inscription: "Iñigo Zabaleta, MD, es un Oftalmólogo Subespecialista en Cirugía Refractiva de la Universidad Católica Mirandina (Colombia) y la Universidad de Montealto (España). Actualmente se desempeña como miembro del Departamento de Córnea y Cirugía Refractiva de la Clínica de Oftalmología Los Robles y como director de su propia compañía de emprendimiento médico Silver Heron Surgical". Please leave a space to place my picture; I will have it taken this week so I don't have it right now, you can just leave the blank spot and I will include it later
The size of the pages is standard "letter" size.
Thanks a lot!

Target Market(s)

PhD Scholars

Font styles to use
Serif

Requirements
Must have
• The "red" color I use on my font. It must be formal but "young".
Nice to have
• I like to keep the design clean, kind of "formal with a young" touch so to speak. I really like gray colors, so it would be nice to have broad areas of gray. I love geometrical designs.
I have uploaded a very early version a friend of mine made (it even had a different title); this can be a starting point for you to work on, but I am more than open to suggestions and new ideas.
Should not have
• Please don't use my whole name, Iñigo Zabaleta is fine. I don't like ALL CAPITALS.

```html
<!DOCTYPE html>
<html lang="es">
<head>
<meta charset="utf-8">
<title>Cubierta de tesis doctoral – Iñigo Zabaleta</title>
<link rel="stylesheet" href="https://fonts.googleapis.com/css2?family=Barlow:wght@400;600&family=Barlow+Condensed:wght@600&display=swap">
<style>
  :root{
    --stage:#e4e4e4;
    --cover-dark:#363636;
    --cover-line:#4b4b4b;
    --hex-stroke:#c9c9c9;
    --panel-light:#cfcfcf;
    --hex-mid:#474747;
    --accent-red:#4a1219;
    --brand-maroon:#8a1538;
    --rule-start:#f2a500;
    --rule-end:#d4202c;
    --title-white:#ffffff;
    --author-gray:#bdbdbd;
    --bio-text:#e2e2e2;
  }
  *{box-sizing:border-box;margin:0;padding:0}
  html,body{width:1200px;height:1142px;overflow:hidden;background:var(--stage)}
  .stage{position:relative;width:1200px;height:1142px}
  .cover{position:absolute;top:221px;width:540px;height:700px;background:var(--cover-dark);overflow:hidden;box-shadow:0 6px 18px rgba(0,0,0,.18)}
  .cover--front{left:40px}
  .cover--back{left:620px}
  .cover__art{position:absolute;inset:0;width:540px;height:700px}

  .title-block{position:absolute;left:58px;top:52px;width:240px}
  .title-rule{height:3px;width:140px;background:linear-gradient(90deg,var(--rule-start),var(--rule-end))}
  .title{margin:12px 0 10px;font-family:"Barlow Condensed",sans-serif;font-weight:600;font-size:25px;line-height:1.02;color:var(--title-white)}
  .author{margin-top:8px;font-family:"Barlow",sans-serif;font-weight:400;font-size:19px;letter-spacing:.5px;color:var(--author-gray)}

  .university{position:absolute;left:330px;top:62px;width:210px;text-align:center}
  .university__mark{display:block;margin:0 auto 10px;width:54px;height:54px;border:2px solid var(--brand-maroon);border-radius:50%}
  .university__name{font-family:"Barlow Condensed",sans-serif;font-weight:600;font-size:17px;color:var(--brand-maroon)}
  .school{margin-top:16px;font-family:"Barlow Condensed",sans-serif;font-weight:600;font-size:13px;color:#3a3a3a}

  .bio{position:absolute;left:142px;top:350px;width:260px;text-align:center;font-family:"Barlow",sans-serif;color:var(--bio-text)}
  .bio__name{font-weight:600;font-size:15px;margin-bottom:2px}
  .bio__text{font-weight:400;font-size:12.5px;line-height:1.42}
</style>
</head>
<body>
<main class="stage">

  <section class="cover cover--front" aria-label="Cubierta frontal">
    <svg class="cover__art" viewBox="0 0 540 700" aria-hidden="false">
      <defs>
        <linearGradient id="eyeTone" x1="0" y1="0" x2="1" y2="1">
          <stop offset="0" stop-color="#9a9a9a"/>
          <stop offset=".5" stop-color="#5e5e5e"/>
          <stop offset="1" stop-color="#b4b4b4"/>
        </linearGradient>
      </defs>
      <!-- light panel -->
      <polygon points="385,0 540,0 540,318 393,312 299,150" fill="var(--panel-light)"/>
      <polyline points="368,0 282,150 380,324 540,330" fill="none" stroke="var(--hex-stroke)" stroke-width="2"/>
      <!-- bottom mid hex -->
      <polygon points="170,683 330,683 342,700 158,700" fill="var(--hex-mid)"/>
      <!-- red corner -->
      <polygon points="448,600 540,592 540,700 452,700 410,648" fill="var(--accent-red)"/>
      <!-- framing lines -->
      <polyline points="340,368 380,324" fill="none" stroke="var(--hex-stroke)" stroke-width="2"/>
      <polyline points="430,515 540,500" fill="none" stroke="var(--cover-line)" stroke-width="2"/>
      <polyline points="430,515 410,648 448,600" fill="none" stroke="var(--hex-stroke)" stroke-width="2"/>
      <polyline points="158,700 172,676 328,676 345,700" fill="none" stroke="var(--hex-stroke)" stroke-width="2"/>
      <polyline points="410,648 380,700" fill="none" stroke="var(--hex-stroke)" stroke-width="2"/>
      <!-- eye hexagon -->
      <polygon points="70,515 160,358 340,358 430,515 340,672 160,672" fill="none" stroke="var(--hex-stroke)" stroke-width="2"/>
      <polygon role="img" aria-label="Fotografía en blanco y negro de un ojo de perfil con córnea abombada" points="92,515 171,378 329,378 408,515 329,652 171,652" fill="url(#eyeTone)"/>
    </svg>

    <div class="title-block">
      <div class="title-rule"></div>
      <h1 class="title">Diseño, desarrollo y validación de una encuesta para evaluar el compromiso visual y emocional subjetivos en pacientes con Queratocono</h1>
      <div class="title-rule"></div>
      <p class="author">Iñigo Zabaleta</p>
    </div>

    <div class="university">
      <span class="university__mark"></span>
      <p class="university__name">Universidad de Montealto</p>
      <p class="school">Escuela de Doctorado Montealto</p>
    </div>
  </section>

  <section class="cover cover--back" aria-label="Contracubierta">
    <svg class="cover__art" viewBox="0 0 540 700">
      <g fill="none" stroke="var(--cover-line)" stroke-width="2">
        <polyline points="340,0 262,140 75,135 0,30"/>
        <polyline points="75,135 175,292"/>
        <polygon points="78,460 175,292 369,292 466,460 369,628 175,628"/>
        <polyline points="78,460 0,455"/>
        <polyline points="175,628 140,700"/>
        <polyline points="369,628 400,700"/>
        <polyline points="466,460 540,470"/>
      </g>
      <rect role="img" aria-label="Espacio reservado para la fotografía del autor" x="225" y="245" width="82" height="95" fill="#d9d9d9"/>
    </svg>

    <div class="bio">
      <p class="bio__name">Iñigo Zabaleta, MD,</p>
      <p class="bio__text">es un Oftalmólogo Subespecialista en Cirugía Refractiva de la Universidad Católica Mirandina (Colombia) y la Universidad de Montealto (España). Actualmente se desempeña como miembro del Departamento de Córnea y Cirugía Refractiva de la Clínica de Oftalmología Los Robles y como director de su propia compañía de emprendimiento médico Silver Heron Surgical</p>
    </div>
  </section>

</main>
</body>
</html>
```